Stationery Refresh For Local Mortgage Broker

We want to modernise and standardise our stationery, including: letterhead, presentation folder, email signature and business card.

The new stationery should be a more modern and professional take on our existing colour scheme and brand. (We do not want a complete overhaul.) A folder of approved stock photos can be found here: https://files.cloudvaultex.com/share/7kTmQzR2wY9bLp4nVx3cHd8sJf6gNa1eU/view?usp=sharing

Our current website is: www.brellanfinco.com.au but we will be updating this to be consistent with our new stationery.

We are open to *very slight* tweaks to our logo if you feel it needs modernising, but overall we would like to maintain consistent colour scheme.

> Letterhead

418 Wenlock Parade,
Geelong, VIC, 3220
ABN: 37 158 402 963
Australian Credit License: 712893

(03) 5019 6284
www.brellanfinco.com.au

> Presentation Folder

418 Wenlock Parade,
Geelong, VIC, 3220
(03) 5019 6284
www.brellanfinco.com.au

ABN: 37 158 402 963

> Email Signature

Dylan Ferraway
Director
M. 0417 250 964
P. (03) 5019 6284
www.brellanfinco.com.au
418 Wenlock Parade,
Geelong, VIC, 3220

ABN: 37 158 402 963

(you can also include a photo if you like: https://brellanfinco.com.au/wp-content/uploads/2020/12/Dylan-Ferraway.png.webp)

> Business Card

Dylan Ferraway
Director
M. 0417 250 964
P. (03) 5019 6284
www.brellanfinco.com.au
418 Wenlock Parade,
Geelong, VIC, 3220

ABN: 37 158 402 963

Additional information...

If it's useful/relevant, the services we offer are: Home Loans, Investment Loans, Refinance, Debt Consolidation, Commercial Finance, Vehicle Loans
(You may choose to use this in any of the designs)

Target Market(s)

Home Buyers and Investors

Industry/Entity Type

Mortgage broking/property/real estate

Requirements
Must have
• At least somewhat consistent with our current site (yet meaningfully modernized)
Should not have
• dramatically different logo or colourscheme overhauls

```html
<!DOCTYPE html>
<html lang="en">
<head>
<meta charset="utf-8">
<title>Brellan Finance – Letterhead</title>
<link rel="stylesheet" href="https://fonts.googleapis.com/css2?family=Lato:wght@400;700;900&family=Montserrat:wght@500&family=Poppins:wght@300;400&display=swap">
<style>
  :root {
    --backdrop: #7a787a;
    --paper: #efefef;
    --paper-shade: #e4e4e4;
    --brand-red: #9a0a10;
    --brand-red-deep: #7d050a;
    --charcoal: #48484a;
    --band-light: #e2e2e4;
    --ink: #151515;
    --ink-soft: #4a4a4a;
    --white: #ffffff;
  }
  * { margin: 0; padding: 0; box-sizing: border-box; }
  html, body { width: 1200px; height: 803px; overflow: hidden; }
  body { background: var(--backdrop); position: relative; }

  .letterhead {
    position: absolute; left: 329px; top: 20px;
    width: 541px; height: 763px;
    background: linear-gradient(135deg, var(--paper) 0%, var(--paper-shade) 100%);
    box-shadow: 0 6px 18px rgba(0,0,0,.28);
    overflow: hidden;
    font-family: 'Lato', sans-serif;
    color: var(--ink);
  }

  .header-band-light { position: absolute; left: 0; top: 49px; width: 541px; height: 36px; background: var(--band-light); }
  .header-band { position: absolute; left: 0; top: 49px; width: 360px; height: 44px; }
  .brand-block { position: absolute; left: 24px; top: 30px; width: 190px; height: 70px; }
  .brand-name {
    position: absolute; left: 214px; top: 62px; width: 128px;
    font-family: 'Lato', sans-serif; font-weight: 700;
    font-size: 13px; line-height: 16px; letter-spacing: 0;
    color: var(--white); text-align: center; white-space: nowrap;
  }

  .registration {
    position: absolute; left: 376px; top: 21px;
    font-family: 'Poppins', sans-serif; font-weight: 300;
    font-size: 9.3px; line-height: 12px; color: var(--ink-soft);
  }

  .letter-date {
    position: absolute; left: 377px; top: 129px;
    font-family: 'Montserrat', sans-serif; font-weight: 500;
    font-size: 10.2px; color: var(--ink-soft);
  }
  .salutation {
    position: absolute; left: 42px; top: 148px;
    font-weight: 900; font-size: 13.5px; letter-spacing: -0.3px;
  }
  .letter-body {
    position: absolute; left: 42px; top: 190px; width: 452px;
    font-size: 12.2px; line-height: 20px; color: var(--ink);
  }
  .letter-body p + p { margin-top: 20px; }

  .network-texture {
    position: absolute; left: 0; top: 583px; width: 541px; height: 165px;
    background: linear-gradient(180deg, rgba(220,220,220,0) 0%, rgba(210,210,212,.45) 100%);
  }

  .sign-off {
    position: absolute; left: 42px; top: 601px;
    font-family: 'Poppins', sans-serif; font-size: 12px; color: var(--brand-red);
  }
  .signature {
    position: absolute; left: 399px; top: 627px; width: 93px; height: 37px;
    background: linear-gradient(90deg, rgba(60,60,60,.12), rgba(60,60,60,.2));
    border-radius: 3px;
  }
  .contact {
    position: absolute; left: 376px; top: 683px;
    font-family: 'Poppins', sans-serif; font-weight: 300; font-style: normal;
    font-size: 9.3px; line-height: 12px; color: var(--ink-soft);
  }
  .contact .phone { margin-top: 12px; }

  .footer-bar { position: absolute; left: 0; top: 749px; width: 541px; height: 14px; background: var(--charcoal); }
  .footer-red {
    position: absolute; left: 266px; top: 736px; width: 275px; height: 27px;
    background: var(--brand-red); border-top-left-radius: 12px;
  }
  .footer-red::after {
    content: ""; position: absolute; right: 0; top: 0; width: 38px; height: 27px; background: var(--brand-red-deep);
  }
  .website {
    position: absolute; left: 376px; top: 742px;
    font-family: 'Poppins', sans-serif; font-size: 9.5px; color: var(--white);
  }
</style>
</head>
<body>
  <article class="letterhead">
    <div class="header-band-light"></div>
    <svg class="header-band" viewBox="0 0 360 44" aria-hidden="true">
      <path d="M0 0 H360 L350 30 Q345 44 330 44 H0 Z" fill="var(--charcoal)"/>
    </svg>
    <svg class="brand-block" viewBox="0 0 190 70" aria-hidden="true">
      <path d="M0 0 H188 L190 10 Q170 20 160 44 Q148 70 125 70 H0 Z" fill="var(--brand-red)"/>
      <rect x="0" y="0" width="6" height="70" fill="var(--brand-red-deep)"/>
    </svg>
    <div class="brand-name">Brellan Finance</div>

    <div class="registration">
      ABN: 37 158 402 963<br>
      Australian Credit License: 712893
    </div>

    <div class="letter-date">Date August 00, 2022</div>
    <h1 class="salutation">DEAR MARLOW TENNANT,</h1>

    <div class="letter-body">
      <p>Lorem ipsum dolor sit amet, consectetur adipiscing elit, sed do eiusmod tempor incididunt ut labore et dolore magna aliqua. Ut enim ad minim veniam, quis nostrud exercitation ullamco laboris nisi ut aliquip ex ea commodo consequat. Duis aute irure dolor in reprehenderit in.</p>
      <p>Sed ut perspiciatis unde omnis iste natus error sit voluptatem accusantium doloremque laudantium, totam rem aperiam, eaque ipsa quae ab illo inventore veritatis et quasi architecto beatae vitae dicta sunt explicabo. Nemo enim ipsam voluptatem quia voluptas sit aspernatur aut odit aut fugit, sed quia consequuntur magni dolores eos qui ratione voluptatem sequi nesciunt. Neque porro quisquam est, qui dolorem ipsum quia dolor sit amet, consectetur, adipisci velit, sed quia non numquam eius modi tempora incidunt ut labore et dolore magnam aliquam quaerat voluptatem. Ut enim ad minima veniam, quis nostrum exercitationem ullam corporis suscipit laboriosam, nisi ut aliquid ex ea commodi consequatur.</p>
    </div>

    <div class="network-texture" role="img" aria-label="Faint connected-dots network pattern decorating the lower page"></div>

    <div class="sign-off">Sincerly,</div>
    <div class="signature" role="img" aria-label="Handwritten signature of the sender"></div>

    <address class="contact">
      418 Wenlock Parade,<br>
      Geelong, VIC, 3220
      <div class="phone">(03) 5019 6284</div>
    </address>

    <div class="footer-bar"></div>
    <div class="footer-red"></div>
    <div class="website">www.brellanfinco.com.au</div>
  </article>
</body>
</html>
```